Infografik für Firmendarstellung eines Immobilienunternehmens
Zielgruppe
1. Firma: Immobilienverkauf -> Immobilienakquise / Immobilieneinwertung
2. Firma: Wohnhof 17 -> Immobilienvermittlung / Immobilienmakler
3. Firma: Ziegelbau81 GmbH -> Immobilienhandel / Immobilienentwicklung
Aufgabenstellung
Graphische Darstellung aller 3 Firmen mit jeweiligen Logo und Erklärung -> siehe beigefügte handschriftliche Grafik.

```html
<!DOCTYPE html>
<html lang="de">
<head>
<meta charset="utf-8">
<title>Firmenverbund – Infografik</title>
<link rel="stylesheet" href="https://fonts.googleapis.com/css2?family=EB+Garamond:wght@400;500&display=swap">
<style>
  :root {
    --frame: #ffffff;
    --panel-light: #f1eadb;
    --panel-dark: #e4d9c0;
    --gold: #b8954a;
    --gold-line: #c3a86f;
    --bronze: #a8701f;
    --ink: #141414;
    --mark: #c9ab6a;
  }
  html, body {
    margin: 0;
    padding: 0;
    width: 1200px;
    height: 700px;
    overflow: hidden;
    background: var(--frame);
  }
  .canvas {
    position: relative;
    width: 1200px;
    height: 700px;
    background: var(--frame);
    font-family: "EB Garamond", Georgia, serif;
  }
  .panel {
    position: absolute;
    left: 15px;
    top: 15px;
    width: 1171px;
    height: 670px;
    background: radial-gradient(ellipse at 50% 50%, var(--panel-light) 0%, var(--panel-light) 30%, var(--panel-dark) 100%);
  }
  .connectors {
    position: absolute;
    left: 0;
    top: 0;
  }
  .company {
    position: absolute;
    margin: 0;
  }
  .company-name {
    margin: 0;
    font-weight: 500;
    line-height: 1;
    white-space: nowrap;
  }
  .company-services {
    margin: 0;
    color: var(--gold);
    font-size: 28px;
    line-height: 30px;
    white-space: nowrap;
  }
  .company--sales {
    left: 314px;
    top: 98px;
    width: 560px;
    text-align: center;
  }
  .company--sales .company-name {
    color: var(--bronze);
    font-size: 60px;
  }
  .company--sales .company-services {
    margin-top: 28px;
  }
  .company--brokerage {
    left: 76px;
    top: 344px;
  }
  .company--brokerage .company-name {
    color: var(--ink);
    font-size: 68px;
    font-weight: 400;
    margin-bottom: 42px;
  }
  .company--trade {
    left: 808px;
    top: 385px;
  }
  .company--trade .company-name {
    color: var(--gold);
    font-size: 60px;
    margin-bottom: 8px;
  }
  .group-mark {
    position: absolute;
    left: 495px;
    top: 327px;
    width: 178px;
    height: 138px;
    background: var(--mark);
  }
</style>
</head>
<body>
<main class="canvas">
  <div class="panel"></div>

  <svg class="connectors" width="1200" height="700" viewBox="0 0 1200 700" aria-hidden="true">
    <g fill="none" stroke-linejoin="miter">
      <g stroke="var(--gold-line)" stroke-width="6">
        <polyline points="188,320 188,201 300,201"/>
        <polyline points="878,201 963,201 963,262"/>
        <polyline points="188,548 188,612 965,612 965,540"/>
      </g>
      <g stroke="var(--panel-light)" stroke-width="2">
        <polyline points="188,318 188,201 298,201"/>
        <polyline points="880,201 963,201 963,260"/>
        <polyline points="188,550 188,612 965,612 965,542"/>
      </g>
    </g>
    <g fill="var(--gold-line)">
      <polygon points="298,192 327,201 298,210"/>
      <polygon points="179,316 197,316 188,336"/>
      <polygon points="880,192 851,201 880,210"/>
      <polygon points="954,258 972,258 963,278"/>
      <polygon points="179,552 197,552 188,533"/>
      <polygon points="956,544 974,544 965,525"/>
    </g>
  </svg>

  <section class="company company--sales">
    <h2 class="company-name">Hauswert Nord</h2>
    <p class="company-services">Immobilienaquise | Immobilienbewertung</p>
  </section>

  <div class="group-mark" role="img" aria-label="Platz für das Firmenzeichen des Verbunds"></div>

  <section class="company company--brokerage">
    <h2 class="company-name">Wohnhof 17</h2>
    <p class="company-services">Immobilienvermittlung<br>Immobilienmakler</p>
  </section>

  <section class="company company--trade">
    <h2 class="company-name">Ziegelbau81</h2>
    <p class="company-services">Immobilienhandel<br>Immobilienentwicklung</p>
  </section>
</main>
</body>
</html>
```